Business Card Design for Varnok Facility Services

We are looking for a Business Card Design for the Company "Varnok Facility Services."
Front side:
- Company Logo (small)
- Company Name, address, pohone, website and personal data.
- white background, for text e.g. company colors (blue or green like in the logo)
Please use following data:
Company data:
Varnok Facility Services Tulbrecht
Kirchmattweg 12
6331 Cham
www.varnok-fs.ch
Person data:
Ruben Tulbrecht
Geschäftsführer
+41 76 519 84 60
info@varnok-fs.ch
Back side:
could be colored in blue or green
please use a big logo sing and some smaller icons to say what is all beeing offered in facility services, like cleaning, maintenance cleaning
industrial cleaning, caretaking, gardening, disposal. There is no need for everyone of the icons if there are similar or an icon is standing for more of them.
Cleaning Service
colors to use:
blue: HEX 246BB0
green: HEX 52B33E

```html
<!DOCTYPE html>
<html lang="de">
<head>
<meta charset="utf-8">
<title>Varnok Facility Services – Business Card</title>
<link rel="stylesheet" href="https://fonts.googleapis.com/css2?family=Source+Sans+3:wght@400;600&display=swap">
<style>
  :root {
    --stage: #0e1a21;
    --card: #ffffff;
    --blue: #246bb0;
    --bar-blue: #1769b6;
    --green: #52b33e;
    --ink: #16212b;
  }
  * { box-sizing: border-box; margin: 0; padding: 0; }
  html, body { width: 1200px; height: 960px; overflow: hidden; background: var(--stage); }
  body { position: relative; font-family: "Source Sans 3", sans-serif; color: var(--ink); }

  .card {
    position: absolute;
    left: 286px;
    width: 629px;
    height: 360px;
    background: var(--card);
    overflow: hidden;
  }
  .card--front { top: 109px; }
  .card--back { top: 492px; }

  /* Front */
  .side-bar {
    position: absolute;
    left: 30px; top: 0;
    width: 28px; height: 315px;
    background: var(--bar-blue);
    border-radius: 0 0 14px 14px;
  }
  .person { position: absolute; left: 66px; top: 64px; }
  .person__name { font-size: 24px; font-weight: 600; line-height: 1.1; letter-spacing: 0.1px; }
  .person__role { font-size: 19px; font-weight: 400; margin-top: 4px; }

  .brand-small {
    position: absolute; right: 22px; top: 72px;
    display: flex; align-items: center; gap: 10px;
  }
  .brand-small__dot { width: 26px; height: 26px; border-radius: 50%; background: var(--green); }
  .brand-small__name { font-size: 22px; font-weight: 600; color: var(--blue); white-space: nowrap; }

  .contacts { position: absolute; left: 0; top: 190px; list-style: none; }
  .contacts li {
    display: flex; align-items: center;
    height: 26.3px;
    font-size: 16.8px;
  }
  .contacts svg { width: 16px; height: 16px; margin-left: 36px; margin-right: 14px; flex: none; }

  /* Back */
  .brand-large {
    position: absolute; left: 0; right: 0; top: 140px;
    display: flex; justify-content: center; align-items: center; gap: 14px;
  }
  .brand-large__dot { width: 44px; height: 44px; border-radius: 50%; background: var(--green); }
  .brand-large__name { font-size: 34px; font-weight: 600; color: var(--blue); white-space: nowrap; }

  .services { position: absolute; top: 268px; left: 0; right: 0; list-style: none; }
  .services li {
    position: absolute;
    display: flex; align-items: center;
    font-size: 17px; white-space: nowrap; height: 22px;
  }
  .services svg { width: 15px; height: 15px; position: absolute; left: -30px; top: 4px; }
  .col-1 { left: 70px; } .col-2 { left: 304px; } .col-3 { left: 515px; }
  .row-1 { top: 0; } .row-2 { top: 26px; }

  .edge-tab {
    position: absolute; top: 280px;
    width: 22px; height: 28px;
    background: var(--bar-blue);
  }
  .edge-tab--left { left: 0; border-radius: 0 14px 14px 0; }
  .edge-tab--right { right: 0; border-radius: 14px 0 0 14px; }
</style>
</head>
<body>

<svg width="0" height="0" style="position:absolute">
  <defs>
    <symbol id="sparkle" viewBox="0 0 20 20">
      <path d="M10 0 L12 8 L20 10 L12 12 L10 20 L8 12 L0 10 L8 8 Z" fill="#246bb0"/>
    </symbol>
  </defs>
</svg>

<section class="card card--front" aria-label="Front side">
  <div class="side-bar"></div>

  <div class="person">
    <h1 class="person__name">Ruben Tulbrecht</h1>
    <p class="person__role">Geschäftsführer</p>
  </div>

  <div class="brand-small">
    <span class="brand-small__dot"></span>
    <span class="brand-small__name">Varnok Facility Services</span>
  </div>

  <ul class="contacts">
    <li>
      <svg viewBox="0 0 24 24" fill="#fff"><path d="M6.6 10.8a15.1 15.1 0 0 0 6.6 6.6l2.2-2.2a1 1 0 0 1 1-.25 11.4 11.4 0 0 0 3.6.6 1 1 0 0 1 1 1V20a1 1 0 0 1-1 1A17 17 0 0 1 3 4a1 1 0 0 1 1-1h3.5a1 1 0 0 1 1 1c0 1.25.2 2.45.6 3.6a1 1 0 0 1-.25 1z"/></svg>
      +41 76 519 84 60
    </li>
    <li>
      <svg viewBox="0 0 24 24" fill="none" stroke="#fff" stroke-width="2"><rect x="2" y="5" width="20" height="14"/><path d="M2 5l10 8 10-8M2 19l7-7M22 19l-7-7"/></svg>
      info@varnok-fs.ch
    </li>
    <li>
      <svg viewBox="0 0 24 24" fill="none" stroke="#fff" stroke-width="2"><circle cx="12" cy="12" r="10"/><path d="M2 12h20M12 2a15 15 0 0 1 0 20M12 2a15 15 0 0 0 0 20"/></svg>
      www.varnok-fs.ch
    </li>
    <li>
      <svg viewBox="0 0 24 24" fill="none" stroke="#fff" stroke-width="2"><path d="M12 18s-6-6-6-10a6 6 0 0 1 12 0c0 4-6 10-6 10z"/><circle cx="12" cy="8" r="2"/><ellipse cx="12" cy="20" rx="8" ry="2"/></svg>
      Kirchmattweg 12, 6331 Cham
    </li>
  </ul>
</section>

<section class="card card--back" aria-label="Back side">
  <div class="brand-large">
    <span class="brand-large__dot"></span>
    <span class="brand-large__name">Varnok Facility Services</span>
  </div>

  <ul class="services">
    <li class="col-1 row-1"><svg><use href="#sparkle"/></svg>Like cleaning</li>
    <li class="col-1 row-2"><svg><use href="#sparkle"/></svg>Maintenance cleaning</li>
    <li class="col-2 row-1"><svg><use href="#sparkle"/></svg>Industrial cleaning</li>
    <li class="col-2 row-2"><svg><use href="#sparkle"/></svg>Caretaking</li>
    <li class="col-3 row-1"><svg><use href="#sparkle"/></svg>Gardening</li>
    <li class="col-3 row-2"><svg><use href="#sparkle"/></svg>Disposal</li>
  </ul>

  <span class="edge-tab edge-tab--left"></span>
  <span class="edge-tab edge-tab--right"></span>
</section>

</body>
</html>
```